Career development coaching - school lever to adults, needs a business card

Tandem Lark - An independent Career Advice business that provides 1-2-1 advice,for career development, entrepreneurial support and workshops needs a business card. Our clients of all ages (school leaver to adults looking for a career move) and universities and colleges. We would like the card to be double-sided with a modern, professional look. Looking for something professional yet very creative and original. Want a standard size business card that inspires a second look because it stands out from the rest.

One side of the card to have a design incorporating the logo with Tandem Lark name with the strap line “Helping you find your future” and space for the company website

Other side of the card to the logo/Tandem Lark name and the usual contact information:
Individual Name
Job Title (for example, Director)
Phone number
Email address
Company website address

Facebook, LinkedIn and Twitter links will need to go somewhere (back or front!)

The design will be used for 3 individuals so should be editable so that we can update as needed/as we grow.

Attached is the company logo/colours to be incorporated.

Target Market(s)

1-2-1 advice,for career development, entrepreneurial support and workshops needs a business card. Our clients of all ages (school leaver to adults looking for a career move) and universities and colleges.

Industry/Entity Type

Consulting

Contact Information for Business Card

Individual Name
Phone number
Email address
Company website address

Font styles to use
Sans Serif

Colors
0255a3
3176b5
faa54b
f78f20
85acd3
cfdeed

Requirements
Must have
• use the Tandem Lark Logo in some way - using the colours and the blue/orange palette
• For the logo - hope this makes sense to someone or if they direclty relate to the logo image attached!
• For the Orange:- Pantone 1585 C
• In CMYK : C3 M71 Y100 K0
• For the Blue:- 100% Pantone 7469 C
• In CMYK : C100 M62 Y27 K7
• Please feel free to contact me with any questions for more info
Nice to have
• happy to see any creative designs
Should not have
• Nothing too traditional,

```html
<!DOCTYPE html>
<html lang="en">
<head>
<meta charset="utf-8">
<title>Tandem Lark – Business Card</title>
<link href="https://fonts.googleapis.com/css2?family=Montserrat:wght@400;500;600&display=swap" rel="stylesheet">
<style>
  :root{
    --backdrop:#d1d2d4;
    --frame:#8a8b8d;
    --brand-blue:#035a8a;
    --brand-orange:#f07a23;
    --paper:#ffffff;
    --shadow:rgba(0,0,0,.35);
  }
  *{margin:0;padding:0;box-sizing:border-box}
  html,body{width:1200px;height:928px;overflow:hidden}
  body{
    background:var(--backdrop);
    font-family:"Montserrat",sans-serif;
    position:relative;
  }
  .board{position:absolute;inset:2px;border:1.5px solid var(--frame)}
  .card{
    position:absolute;top:97px;width:419px;height:733px;
    box-shadow:8px 9px 10px var(--shadow);
    overflow:hidden;
  }
  .card--front{left:163px;background:var(--paper)}
  .card--back{left:618px;background:var(--brand-blue)}
  .line{position:absolute;left:0;right:0;text-align:center;white-space:nowrap}

  /* Front */
  .front-brand{position:absolute;left:0;right:0;top:0;height:359px}
  .brand-dot{
    position:absolute;left:50%;top:77px;width:143px;height:143px;margin-left:-71px;
    border-radius:50%;background:var(--brand-blue);
  }
  .brand-name{
    top:245px;height:44px;line-height:44px;
    font-size:40px;font-weight:600;letter-spacing:1.5px;
    font-variant:small-caps;color:var(--brand-blue);
  }
  .accent-rule{position:absolute;left:0;right:0;top:359px;height:6px;background:var(--brand-orange)}
  .contact-panel{
    position:absolute;left:0;right:0;top:365px;bottom:0;background:var(--brand-blue);
    color:var(--paper);
  }
  .contact-panel .line{height:24px;line-height:24px;font-size:19px}
  .person-name{top:59px;font-size:26px!important;font-weight:600;color:var(--brand-orange);letter-spacing:.3px}
  .person-title{top:87px;font-size:18px!important}
  .icon-row{position:absolute;left:0;right:0;display:flex;justify-content:center;gap:5px}
  .icon-row--contact{top:127px}
  .icon-row--social{top:236px}
  .icon-row svg{width:13px;height:13px;display:block}
  .social-dot{width:9px;height:9px;border-radius:50%;background:var(--brand-orange);margin:2px 3px}
  .hl{color:var(--brand-orange)}

  /* Back */
  .back-dot{
    position:absolute;left:50%;top:247px;width:190px;height:190px;margin-left:-95px;
    border-radius:50%;background:var(--paper);
  }
  .back-name{top:462px;line-height:40px;font-size:32px;font-weight:600;color:var(--paper);letter-spacing:1px}
  .strapline{top:508px;line-height:24px;font-size:17px;font-weight:400;color:var(--paper);letter-spacing:.5px}
  .back-web{top:664px;line-height:26px;font-size:21px;color:var(--paper);letter-spacing:.8px}
</style>
</head>
<body>
<div class="board"></div>

<section class="card card--front">
  <div class="front-brand">
    <div class="brand-dot"></div>
    <div class="line brand-name">Tandem Lark</div>
  </div>
  <div class="accent-rule"></div>
  <div class="contact-panel">
    <div class="line person-name">Maren Holt</div>
    <div class="line person-title">Director</div>
    <div class="icon-row icon-row--contact" aria-hidden="true">
      <svg viewBox="0 0 16 16"><path d="M4 1.5l2.3 3-1.4 1.6c.9 2 2.4 3.6 4.5 4.5l1.6-1.4 3 2.3-1.4 2.5C6.8 14 2 9.2 1.5 3z" fill="#f07a23"/></svg>
      <svg viewBox="0 0 16 16"><rect x="1.5" y="3.5" width="13" height="9" fill="none" stroke="#f07a23" stroke-width="1.6"/><path d="M1.5 3.5l6.5 5 6.5-5" fill="none" stroke="#f07a23" stroke-width="1.6"/></svg>
      <svg viewBox="0 0 16 16"><g fill="none" stroke="#f07a23" stroke-width="1.4"><circle cx="8" cy="8" r="6.3"/><ellipse cx="8" cy="8" rx="2.8" ry="6.3"/><path d="M1.7 8h12.6"/></g></svg>
    </div>
    <div class="line" style="top:153px">+330 5182-4437</div>
    <div class="line" style="top:176px">info@tandemlark.com</div>
    <div class="line" style="top:198px">www.<span class="hl">tandemlark</span>.com</div>
    <div class="icon-row icon-row--social" aria-hidden="true">
      <span class="social-dot"></span><span class="social-dot"></span><span class="social-dot"></span>
    </div>
    <div class="line" style="top:256px">tandemlark.com</div>
    <div class="line" style="top:278px">@tandemlark.com</div>
    <div class="line" style="top:301px">@tandemlark.com</div>
  </div>
</section>

<section class="card card--back">
  <div class="back-dot"></div>
  <div class="line back-name">Tandem Lark</div>
  <div class="line strapline">Helping you find your future</div>
  <div class="line back-web">www.<span class="hl">tandemlark</span>.com</div>
</section>
</body>
</html>
```